I need a flyer that is professional, advertises and informs people about my health coaching practice. I am a Nationally Board Certified Health and Wellness Coach, lifestyle medicine certified and a lifestyle coach for the NHQ's Glucose Steady Initiative. I have my Master's Degree in Counseling Psychology. The final design should communicate evidence based health coaching that is self-directed and aimed at creating lasting health behavioral changes designed to enhance well-being. I am very open in terms of design but really would like a professional look to the flyer. I did want my contact information on the flyer: dana@vitalpathrecords.com and (217) 555-0148

Target Market(s)

Adults looking to improve their health, decrease risk factors for lifestyle disease, reduce weight, make better lifestyle choices to improve well-being.

Industry/Entity Type

Health And Wellness

Font styles to use
Sans Serif

Colors

Designer to choose colors to be used in the design.

Requirements
Must have
• Services offered, a professional feel, Dana Morrow Health Coaching (name of my practice), my phone number (217) 555-0148 and email: dana@vitalpathrecords.com, location: 1873 W Larkfield Avenue Bloomington IL 61709 my website: danamorrow.com to schedule appointments
Nice to have
• What is Health Coaching? Health and Wellness Coaches partner with clients seeking self-directed, lasting changes, aligned with their values, which promote health and wellness and, thereby, enhance well-being. In the course of their work health and wellness coaches display unconditional positive regard for their clients and a belief in their capacity for change, and honoring that each client is an expert on his or her life, while ensuring that all interactions are respectful and non-judgmental.

```html
<!DOCTYPE html>
<html lang="en">
<head>
<meta charset="utf-8">
<title>Dana Morrow Health Coaching</title>
<link rel="stylesheet" href="https://fonts.googleapis.com/css2?family=Roboto:wght@300;400&family=Archivo+Black&family=Roboto+Condensed:wght@700&family=Arimo:wght@700&family=Ubuntu:wght@400;500;700&display=swap">
<style>
  :root {
    --teal: #1ba6bd;
    --teal-deep: #05a7bf;
    --orange: #f47b20;
    --ink-grey: #8c8c8c;
    --btn-dark: #4b4b4b;
    --white: #ffffff;
    --rule: rgba(255,255,255,0.55);
  }
  * { margin: 0; padding: 0; box-sizing: border-box; }
  html, body { width: 869px; height: 1200px; overflow: hidden; background: var(--white); }
  .flyer { position: relative; width: 869px; height: 1200px; overflow: hidden; font-family: "Ubuntu", sans-serif; }

  .hero { position: absolute; left: 0; top: 0; width: 869px; height: 542px;
    background: linear-gradient(160deg, #ececec 0%, #f7f7f7 35%, #ffffff 70%); }
  .hero-photo { position: absolute; left: 370px; top: 10px; width: 290px; height: 528px; z-index: 0;
    background: radial-gradient(ellipse at 50% 50%, #3a3a3a 0%, #4a4a4a 40%, rgba(90,90,90,0.35) 68%, rgba(255,255,255,0) 85%); }
  .hero > *:not(.hero-photo) { z-index: 1; }

  .headline { position: absolute; left: 54px; top: 52px; color: var(--teal); line-height: 1; }
  .headline .light { display: block; font-family: "Roboto", sans-serif; font-weight: 300; font-size: 41px; letter-spacing: -0.6px; }
  .headline .bold { display: block; font-family: "Archivo Black", sans-serif; font-size: 43px; margin-top: 0; letter-spacing: 0.5px; line-height: 40px; }

  .services { position: absolute; left: 55px; top: 224px; list-style: none; }
  .services li { display: flex; align-items: center; height: 35.5px; font-family: "Arimo", sans-serif; font-weight: 700; font-size: 17px; color: var(--ink-grey); }
  .services svg { width: 29px; height: 29px; margin-right: 6px; }

  .tagline { position: absolute; left: 55px; top: 362px; font-family: "Roboto", sans-serif; font-weight: 300; font-size: 23px; line-height: 28px; color: var(--teal); }
  .tagline em { font-style: normal; color: var(--orange); font-weight: 400; }

  .practice { position: absolute; right: 39px; top: 50px; text-align: right; font-family: "Roboto Condensed", sans-serif; font-weight: 700; font-size: 21px; line-height: 24px; }
  .practice .first { color: var(--teal); display: block; }
  .practice .second { color: #7d7d7d; display: block; }
  .phone { position: absolute; right: 39px; top: 115px; display: flex; align-items: center; gap: 5px; font-family: "Roboto Condensed", sans-serif; font-weight: 700; font-size: 14.5px; color: #a2a2a2; }

  .contact-band { position: absolute; left: 0; top: 542px; width: 869px; height: 58px; background: var(--orange);
    display: flex; align-items: center; justify-content: center; gap: 18px; color: var(--white); font-size: 13px; }

  .appointments { position: absolute; left: 0; top: 600px; width: 869px; height: 600px; background: var(--teal-deep); color: var(--white); }
  .appointments h2 { position: absolute; left: 57px; top: 40px; font-size: 27px; font-weight: 700; letter-spacing: 0.3px; }
  .group-title { position: absolute; font-size: 18px; font-weight: 700; line-height: 25px; padding-bottom: 6px; border-bottom: 1.5px solid var(--rule); }
  .card { position: absolute; width: 380px; }
  .card h4 { font-size: 15.5px; font-weight: 700; line-height: 20px; }
  .card p { font-size: 14px; line-height: 19.2px; margin-top: 6px; font-weight: 400; }
  .book { position: absolute; display: flex; height: 48px; border-radius: 6px; overflow: hidden; font-size: 17px; }
  .book .action { width: 71px; background: var(--orange); display: flex; align-items: center; justify-content: center; font-weight: 700; }
  .book .terms { background: var(--btn-dark); display: flex; align-items: center; padding: 0 14px 0 8px; font-family: "Roboto", sans-serif; font-weight: 300; font-size: 17px; }
</style>
</head>
<body>
<div class="flyer">
  <section class="hero">
    <div class="hero-photo" role="img" aria-label="Photo of a smiling woman in a black tracksuit doing a forward lunge stretch"></div>

    <h1 class="headline">
      <span class="light">HEALTH COACHING IS</span>
      <span class="bold">EMBRACING</span>
      <span class="bold">YOUR HEALTH</span>
    </h1>

    <ul class="services">
      <li><svg viewBox="0 0 29 29"><circle cx="14.5" cy="14.5" r="14" fill="#f47b20"/><path d="M8.5 15l4 4 8-9" fill="none" stroke="#fff" stroke-width="3" stroke-linecap="round" stroke-linejoin="round"/></svg>Health Coaching</li>
      <li><svg viewBox="0 0 29 29"><circle cx="14.5" cy="14.5" r="14" fill="#f47b20"/><path d="M8.5 15l4 4 8-9" fill="none" stroke="#fff" stroke-width="3" stroke-linecap="round" stroke-linejoin="round"/></svg>Wellness Experience</li>
      <li><svg viewBox="0 0 29 29"><circle cx="14.5" cy="14.5" r="14" fill="#f47b20"/><path d="M8.5 15l4 4 8-9" fill="none" stroke="#fff" stroke-width="3" stroke-linecap="round" stroke-linejoin="round"/></svg>Active Coaching</li>
    </ul>

    <p class="tagline">Let us help you build<br>the <em>healthy life</em> you deserve!</p>

    <div class="practice"><span class="first">Dana Morrow</span><span class="second">Health Coaching</span></div>
    <div class="phone">(217) 555-0148
      <svg width="20" height="20" viewBox="0 0 20 20"><circle cx="10" cy="10" r="9" fill="none" stroke="#a2a2a2" stroke-width="1.4"/><path d="M7 5.5l1.6 2.3-1 1.2c.6 1.3 1.5 2.2 2.8 2.8l1.2-1 2.3 1.6-.8 1.8c-3.6-.2-6.8-3.4-7-7z" fill="none" stroke="#a2a2a2" stroke-width="1.2" stroke-linejoin="round"/></svg>
    </div>
  </section>

  <div class="contact-band">
    <span>Email: dana@vitalpathrecords.com</span><span>|</span>
    <span>1873 W Larkfield Avenue Bloomington IL 61709</span><span>|</span>
    <span>danamorrow.com</span>
  </div>

  <section class="appointments">
    <h2>Appointment Types</h2>

    <h3 class="group-title" style="left:55px; top:97px; width:756px;">Health Coaching Initial Consultation</h3>

    <div class="card" style="left:55px; top:142px;">
      <h4>Health Coaching Data Collection</h4>
      <p>Evidence based health coaching is based<br>in data. With the appropriate data, we can<br>work together to reduce your risk for lifestyle<br>disease the best wa…</p>
    </div>
    <div class="book" style="left:56px; top:264px;"><span class="action">Book</span><span class="terms">1hr/$99</span></div>

    <div class="card" style="left:459px; top:142px; width:380px;">
      <h4>Health Coaching Initial Collection</h4>
      <p>Want to know if health coaching is right for you? I invite<br>you to schedule an initial consultation with me. During<br>this session, we will discuss your..</p>
    </div>
    <div class="book" style="left:460px; top:264px;"><span class="action">Book</span><span class="terms">30min/free</span></div>

    <h3 class="group-title" style="left:55px; top:346px; width:378px;">Health Coaching Individual<br>30 Minute Session</h3>
    <h3 class="group-title" style="left:460px; top:346px; width:378px;">Health Coaching 6 Session<br>Package</h3>

    <div class="card" style="left:55px; top:416px;">
      <h4>Individual Health Coaching 30 Minute Session</h4>
      <p style="margin-top:0;">Partner with a Nationally Board Certified Health<br>and Wellness Coach (NBC-HWC) for clients seeking<br>self-directed, lasting changes, aligned with their v…</p>
    </div>
    <div class="book" style="left:56px; top:514px;"><span class="action">Book</span><span class="terms">30min/free</span></div>

    <div class="card" style="left:460px; top:416px; width:400px;">
      <h4>Health Coaching Package-Six 30 Minute Sessions</h4>
      <p style="margin-top:0;">A focused health coaching session on the topics<br>of your choice. Designed to get results, this package<br>is shaped and molded around your goals and progr…</p>
    </div>
    <div class="book" style="left:461px; top:514px;"><span class="action">Book</span><span class="terms">30min/free</span></div>
  </section>
</div>
</body>
</html>
```